Corporate consulting business needs a business card

I want a professional business card.... surprise me

Target Market(s)

Corprorate and Not for Profit firms and organisations

Industry/Entity Type

Consulting

Contact Information for Business Card

Logo
Corporate Consulting Services
On Time, On Budget, Beyond Expectation
Tobin Averley
Director
0427 31 64 92 (Larger)
tobin@ta-advisory.com.au
www.ta-advisory.com.au
include little icons beside the contact info:

- Envelope = email
- Phone = phone
- Globe = website

Font styles to use
Serif
Sans Serif

Requirements
Must have
• Professional and clean
Nice to have
• you tell me

```html
<!DOCTYPE html>
<html lang="en">
<head>
<meta charset="utf-8">
<title>TA Advisory – Business Card</title>
<link rel="stylesheet" href="https://fonts.googleapis.com/css2?family=Arimo:wght@400;700&family=Cinzel:wght@700&family=Cormorant+Garamond:wght@500&display=swap">
<style>
  :root {
    --brown: #4f2c12;
    --brown-line: #3a200c;
    --paper: #ffffff;
    --ink: #1e1e1e;
    --stage: #e9e4de;
    --ghost: #ececec;
  }
  * { box-sizing: border-box; margin: 0; padding: 0; }
  html, body { width: 1200px; height: 428px; overflow: hidden; }
  body {
    background: var(--stage);
    font-family: "Arimo", Arial, sans-serif;
    color: var(--ink);
    position: relative;
  }
  .card {
    position: absolute;
    top: 64px;
    width: 540px;
    height: 300px;
    background: var(--paper);
    box-shadow: 0 4px 14px rgba(0,0,0,.18);
    overflow: hidden;
  }
  .card--front { left: 40px; }
  .card--back { left: 620px; }

  /* front */
  .brand {
    position: absolute; top: 30px; left: 0; right: 0;
    display: flex; align-items: center; justify-content: center; gap: 14px;
  }
  .brand__dot {
    width: 54px; height: 54px; border-radius: 50%;
    border: 4px solid var(--brown);
  }
  .brand__name {
    font-family: "Cormorant Garamond", Georgia, serif;
    font-weight: 500; font-size: 40px; color: var(--brown);
  }
  .tagline {
    position: absolute; top: 128px; left: 0; right: 0; text-align: center;
    font-family: "Cinzel", Georgia, serif; font-weight: 700;
    font-size: 19px; color: var(--ink); letter-spacing: .3px;
  }
  .rule { position: absolute; left: 0; right: 0; height: 1.5px; background: var(--brown-line); }
  .rule--top { top: 163px; }
  .rule--bottom { top: 213px; }
  .name-band {
    position: absolute; top: 168px; left: 0; right: 0; height: 40px;
    background: var(--brown); color: #fff;
    display: flex; align-items: center; justify-content: center; gap: 6px;
  }
  .name-band__name { font-size: 18px; }
  .name-band__role { font-size: 14px; }
  .contacts {
    position: absolute; top: 228px; left: 0; right: 0;
    list-style: none; display: flex; flex-direction: column; align-items: center; gap: 4px;
    font-size: 14px;
  }
  .contacts li { display: flex; align-items: center; gap: 8px; }
  .contacts svg { width: 13px; height: 13px; fill: var(--brown-line); }
  .contacts .phone { font-size: 15px; }

  /* back */
  .back__title {
    position: absolute; top: 52px; left: 42px;
    font-size: 19px; font-weight: 400;
  }
  .back__list {
    position: absolute; top: 92px; left: 42px;
    list-style: none; font-size: 14px; line-height: 22px;
  }
  .back__list li::before { content: "\2022"; margin-right: 8px; }
  .back__web { position: absolute; bottom: 32px; left: 42px; font-size: 14px; }
  .back__ghost {
    position: absolute; right: 26px; top: 140px;
    display: flex; align-items: center; gap: 10px;
    font-family: "Cormorant Garamond", Georgia, serif; font-weight: 500;
    font-size: 30px; color: var(--ghost);
  }
  .back__ghost-dot {
    width: 30px; height: 30px; border-radius: 50%;
    border: 3px solid var(--ghost);
  }
</style>
</head>
<body>
  <section class="card card--front" aria-label="Business card front">
    <div class="brand">
      <span class="brand__dot"></span>
      <span class="brand__name">TA Advisory</span>
    </div>
    <h1 class="tagline">Consulting Services</h1>
    <div class="rule rule--top"></div>
    <div class="name-band">
      <span class="name-band__name">Tobin Averley,</span>
      <span class="name-band__role">Director</span>
    </div>
    <div class="rule rule--bottom"></div>
    <ul class="contacts">
      <li class="phone">
        <svg viewBox="0 0 12 16" aria-hidden="true"><path d="M2 0h8a1 1 0 0 1 1 1v14a1 1 0 0 1-1 1H2a1 1 0 0 1-1-1V1a1 1 0 0 1 1-1zm1 2v7h6V2zm1 9h1v1H4zm2 0h1v1H6zm2 0h1v1H8zm-4 2h1v1H4zm2 0h1v1H6zm2 0h1v1H8z"/></svg>
        0427 31 64 92
      </li>
      <li>
        <svg viewBox="0 0 16 12" aria-hidden="true"><path d="M0 3l8 5 8-5v9H0zM0 0h16v1.5L8 6.5 0 1.5z"/></svg>
        tobin@ta-advisory.com.au
      </li>
      <li>
        <svg viewBox="0 0 16 16" aria-hidden="true"><path d="M8 0a8 8 0 1 0 0 16A8 8 0 0 0 8 0zm5.9 7H11a12 12 0 0 0-1.2-5A6 6 0 0 1 13.9 7zM8 2c.9 1.2 1.6 3 1.8 5H6.2C6.4 5 7.1 3.2 8 2zM6.2 9h3.6c-.2 2-.9 3.8-1.8 5-.9-1.2-1.6-3-1.8-5zM6.2 2A12 12 0 0 0 5 7H2.1a6 6 0 0 1 4.1-5zM2.1 9H5a12 12 0 0 0 1.2 5A6 6 0 0 1 2.1 9zm7.7 5a12 12 0 0 0 1.2-5h2.9a6 6 0 0 1-4.1 5z"/></svg>
        www.ta-advisory.com.au
      </li>
    </ul>
  </section>

  <section class="card card--back" aria-label="Business card back">
    <h2 class="back__title">Corporate Consulting Services</h2>
    <ul class="back__list">
      <li>On Time</li>
      <li>On Budget</li>
      <li>Beyond Expectation</li>
    </ul>
    <div class="back__ghost" aria-hidden="true">
      <span class="back__ghost-dot"></span>
      <span>TA Advisory</span>
    </div>
    <p class="back__web">www.ta-advisory.com.au</p>
  </section>
</body>
</html>
```